Income Tax Flyer - Updates Needed

Just need to update this flyer design and give it a new look. We would like to keep all the same wording but make it stand out a little more. Our selling point is the "Same Day Tax Advance up to $6,000"

Industry/Entity Type

Lending, Small Loans, Tax Services, Title Loans, Personal Loans

```html
<!DOCTYPE html>
<html lang="en">
<head>
<meta charset="utf-8">
<title>Same Day Tax Advance Flyer</title>
<link href="https://fonts.googleapis.com/css2?family=Montserrat:wght@600;700;800&family=Montserrat+Alternates:wght@500;600&display=swap" rel="stylesheet">
<style>
  :root {
    --green: #2c5131;
    --red: #a8242a;
    --panel: #e4e4e4;
    --white: #ffffff;
    --photo-light: #e9ecee;
    --photo-mid: #c9ced3;
    --photo-dark: #5d6470;
  }
  * { margin: 0; padding: 0; box-sizing: border-box; }
  html, body { width: 860px; height: 1200px; overflow: hidden; background: var(--white); }
  .flyer { position: relative; width: 860px; height: 1200px; background: var(--white); font-family: "Montserrat", sans-serif; }
  .shapes { position: absolute; inset: 0; }
  .brand {
    position: absolute; left: 400px; top: 500px; width: 300px; text-align: center;
    font-family: "Montserrat", sans-serif; font-weight: 700; font-size: 30px; line-height: 1.15;
    color: var(--green);
  }
  .headline { position: absolute; left: 0; width: 840px; text-align: center; color: var(--green); font-weight: 800; }
  .headline-main { top: 604px; font-size: 44px; letter-spacing: -0.5px; }
  .headline-amount { top: 656px; font-size: 58px; letter-spacing: -0.5px; }
  .cta-pill {
    position: absolute; left: 70px; top: 736px; width: 706px; height: 48px; border-radius: 24px;
    background: var(--red); color: var(--white); display: flex; align-items: center; justify-content: center; gap: 14px;
    font-weight: 700;
  }
  .cta-pill .lead { font-size: 22px; padding-top: 4px; }
  .cta-pill .accent { font-size: 31px; letter-spacing: 0.5px; }
  .features {
    position: absolute; left: 70px; top: 820px; width: 706px; height: 135px; border-radius: 38px;
    background: var(--panel); display: flex;
  }
  .feature { flex: 1; display: flex; flex-direction: column; align-items: center; padding-top: 8px; }
  .feature-icon {
    width: 56px; height: 56px; border-radius: 50%; background: var(--white); border: 2px solid var(--red);
    display: flex; align-items: center; justify-content: center;
  }
  .feature-label {
    margin-top: 14px; height: 48px; display: flex; align-items: center; text-align: center;
    font-family: "Montserrat Alternates", sans-serif; font-weight: 500; font-size: 19px; line-height: 1.25; color: var(--green);
  }
  .contact-call { position: absolute; left: 212px; top: 986px; width: 146px; text-align: center; }
  .contact-call .line { display: block; color: var(--red); font-family: "Montserrat Alternates", sans-serif; font-weight: 600; font-size: 25px; white-space: nowrap; margin-left: -20px; margin-right: -20px; }
  .contact-call .badge {
    display: block; margin-top: 2px; height: 37px; border-radius: 0 0 8px 8px; background: var(--red); color: var(--white);
    font-family: "Montserrat Alternates", sans-serif; font-weight: 600; font-size: 26px; line-height: 37px;
  }
  .contact-details { position: absolute; left: 455px; top: 978px; width: 200px; text-align: center; }
  .contact-details .phone { color: var(--red); font-family: "Montserrat Alternates", sans-serif; font-weight: 600; font-size: 20px; margin-bottom: 6px; }
  .contact-details .address { color: var(--green); font-family: "Montserrat Alternates", sans-serif; font-weight: 600; font-size: 17px; line-height: 27px; }
</style>
</head>
<body>
<main class="flyer">
  <svg class="shapes" width="860" height="1200" viewBox="0 0 860 1200" aria-hidden="true">
    <defs>
      <linearGradient id="photo-tone" x1="0" y1="0" x2="1" y2="1">
        <stop offset="0" stop-color="var(--photo-light)"/>
        <stop offset="0.55" stop-color="var(--photo-mid)"/>
        <stop offset="1" stop-color="var(--photo-dark)"/>
      </linearGradient>
    </defs>
    <path class="red-swoosh" fill="var(--red)" d="M400,487 C500,432 620,414 700,432 C762,446 800,470 828,496 V566 C780,520 722,484 642,470 C560,456 480,462 400,487 Z"/>
    <path class="green-wave-bottom" fill="var(--green)" d="M19,1004 C150,1090 300,1118 420,1128 C600,1142 760,1140 828,1160 H19 Z"/>
    <path class="red-wave-bottom" fill="var(--red)" d="M19,966 C120,1060 260,1110 400,1126 C290,1118 150,1084 19,1004 Z"/>
  </svg>

  <svg class="shapes" width="860" height="1200" viewBox="0 0 860 1200" role="img" aria-label="Photo of a smiling couple meeting with a financial advisor at a glass table in a bright office">
    <path fill="url(#photo-tone)" d="M19,19 H828 V478 C790,445 740,420 680,410 C620,400 540,405 470,420 C360,450 280,540 175,540 C120,540 60,520 19,468 Z"/>
    <path class="green-wave-top" fill="var(--green)" d="M19,468 C60,520 120,540 175,540 C280,540 360,450 470,420 C360,470 280,582 180,582 C110,582 60,562 19,541 Z"/>
  </svg>

  <div class="brand">Ledgerline<br>Financial</div>

  <h1 class="headline headline-main">SAME DAY TAX ADVANCE</h1>
  <p class="headline headline-amount">UP TO $6,000</p>

  <div class="cta-pill">
    <span class="lead">File your tax and apply for an</span>
    <span class="accent">Easy Advance!</span>
  </div>

  <section class="features">
    <div class="feature">
      <div class="feature-icon">
        <svg width="32" height="32" viewBox="0 0 32 32" fill="none" stroke="var(--green)" stroke-width="2" stroke-linecap="round">
          <circle cx="16" cy="18" r="11"/><path d="M13 4h6M16 4v3M25 9l2-2"/>
          <path d="M18.5 14.5c-.5-1-1.5-1.5-2.5-1.5-1.4 0-2.5.8-2.5 2s1.1 1.7 2.5 2 2.5.9 2.5 2-1.1 2-2.5 2c-1.1 0-2-.5-2.5-1.5M16 11.5v1.5M16 22v1.5"/>
        </svg>
      </div>
      <p class="feature-label">Available in<br>24 Hours or Less</p>
    </div>
    <div class="feature">
      <div class="feature-icon">
        <svg width="32" height="32" viewBox="0 0 32 32" fill="none" stroke="var(--green)" stroke-width="2" stroke-linecap="round" stroke-linejoin="round">
          <path d="M9 19a9 9 0 1 1 12-12"/>
          <path d="M14 9.5c-.4-.7-1-1-1.8-1-1 0-1.7.6-1.7 1.4s.8 1.2 1.7 1.4 1.8.7 1.8 1.5-.8 1.4-1.8 1.4c-.8 0-1.4-.4-1.8-1M12.2 7v1.5M12.2 14.2v1.3"/>
          <path d="M17 27v-4l-3-3a1.5 1.5 0 0 1 2-2l2 2v-7a1.5 1.5 0 0 1 3 0v5l5 1.5c1 .3 1.5 1.2 1.3 2.2L26 27"/>
        </svg>
      </div>
      <p class="feature-label">Choose Your<br>Loan Amount</p>
    </div>
    <div class="feature">
      <div class="feature-icon">
        <svg width="32" height="32" viewBox="0 0 32 32" fill="none" stroke="var(--green)" stroke-width="2" stroke-linecap="round" stroke-linejoin="round">
          <rect x="13" y="4" width="14" height="20" rx="1.5"/>
          <circle cx="20" cy="14" r="3.5"/>
          <path d="M5 22l5-5c1.2-1.2 3-1 4 0l3 3M8 28l3-3h5"/>
        </svg>
      </div>
      <p class="feature-label">Quick and Easy</p>
    </div>
  </section>

  <div class="contact-call">
    <span class="line">Contact Us</span>
    <span class="badge">Today!</span>
  </div>

  <div class="contact-details">
    <p class="phone">Phone Number</p>
    <p class="address">Address line 1</p>
    <p class="address">Address line 2</p>
    <p class="address">Address line 3</p>
  </div>
</main>
</body>
</html>
```